The Book Cover for "Finding the Silver Lantern of Dawn" needs redesigned

First the back ground or art work needs to be replaced or redesigned.
The title Finding the Silver Lantern of Dawn needs to be redesigned so that the words "Finding the" is diminished in size compared to the rest of the title "Silver Lantern of Dawn"
The Sub-title "Tracing the forgotten path of the Evening Wind" needs to be more pronounced and readable.
The authors name needs to be downsized.

```html
<!DOCTYPE html>
<html lang="en">
<head>
<meta charset="UTF-8">
<title>Finding the Silver Lantern of Dawn — Book Cover</title>
<link rel="stylesheet" href="https://fonts.googleapis.com/css2?family=Anton&family=Poppins:wght@300;500&display=swap">
<style>
  :root {
    --page-bg: #f3f3f3;
    --title-yellow: #e8dd00;
    --title-shadow: rgba(0, 0, 0, 0.55);
    --subtitle-white: #f4f1ea;
    --author-white: #ece8e0;
    --night: #0d0a06;
    --dusk-brown: #3a2812;
    --amber: #d98a1c;
    --gold: #f2b640;
    --sun-glow: #fbf0cf;
  }
  * { margin: 0; padding: 0; box-sizing: border-box; }
  html, body {
    width: 1200px;
    height: 1000px;
    overflow: hidden;
    background: var(--page-bg);
  }
  .book-cover {
    position: absolute;
    left: 280px;
    top: 27px;
    width: 640px;
    height: 946px;
    overflow: hidden;
    background: var(--night);
  }
  .cover-art {
    position: absolute;
    inset: 0;
    background:
      radial-gradient(ellipse 46% 22% at 72% 40%, var(--sun-glow) 0%, rgba(251, 240, 207, 0.6) 35%, rgba(242, 182, 64, 0) 100%),
      linear-gradient(180deg,
        var(--night) 0%,
        var(--dusk-brown) 14%,
        #8a5a24 28%,
        var(--gold) 40%,
        var(--amber) 50%,
        #7a4a18 55%,
        #3b3a36 60%,
        #4f4a3c 72%,
        #2a2418 82%,
        var(--night) 92%,
        var(--night) 100%);
  }
  .cover-art::after {
    content: "";
    position: absolute;
    inset: 0;
    background: linear-gradient(90deg, rgba(0,0,0,0.75) 0%, rgba(0,0,0,0.2) 6%, rgba(0,0,0,0) 20%);
  }
  .title-block {
    position: absolute;
    top: 66px;
    left: 0;
    width: 100%;
    text-align: center;
  }
  .title {
    font-family: "Anton", sans-serif;
    font-weight: 400;
    color: var(--title-yellow);
    text-transform: uppercase;
    text-shadow: 2px 3px 4px var(--title-shadow);
    line-height: 1;
  }
  .title-lead {
    display: block;
    font-size: 46px;
    letter-spacing: -0.5px;
  }
  .title-main {
    display: block;
    font-size: 60px;
    letter-spacing: -0.5px;
    margin-top: 2px;
  }
  .subtitle {
    display: inline-block;
    margin-top: 12px;
    padding: 4px 26px 5px;
    font-family: "Poppins", sans-serif;
    font-weight: 500;
    font-size: 19px;
    color: var(--subtitle-white);
    background: linear-gradient(90deg, rgba(0,0,0,0) 0%, rgba(0,0,0,0.45) 12%, rgba(0,0,0,0.4) 85%, rgba(0,0,0,0) 100%);
  }
  .author {
    position: absolute;
    top: 886px;
    left: 0;
    width: 100%;
    text-align: center;
    font-family: "Poppins", sans-serif;
    font-weight: 300;
    font-size: 17px;
    color: var(--author-white);
  }
  .author-rule {
    position: absolute;
    top: 919px;
    left: 288px;
    width: 64px;
    height: 2px;
    background: var(--author-white);
  }
</style>
</head>
<body>
  <article class="book-cover">
    <div class="cover-art" role="img" aria-label="Cover artwork: silhouette of a mother lifting a child against a golden sunset over the sea"></div>
    <header class="title-block">
      <h1 class="title">
        <span class="title-lead">Finding the</span>
        <span class="title-main">Silver Lantern of Dawn</span>
      </h1>
      <p class="subtitle">Tracing the forgotten path of the Evening Wind</p>
    </header>
    <p class="author">R T Miles Ashford</p>
    <div class="author-rule"></div>
  </article>
</body>
</html>
```